Industry: Christian Ministry using Magic, Music and Multimedia to teach gospel

“Lanternfold Ministries brings the Gospel of Jesus Christ, with heart-seeking, biblical accuracy
through live, entertainment-based evangelistic Celebrations."

We are a service that wants to partner with christian religious institutions and churches to teach biblical gospel in a fun and entertaining way using magic.

Design inspiration: https://www.quillmarshwonders.example

DO NOT CONTACT ME PRIVATELY. IT WILL BE IGNORED.

Important:
1. Use only royalty free graphics
2. Use only google fonts
3. A clean, linear layout
4. Do not include search

PAGES

1. Home
2. Shows & Skylark
3. About Lanternfold
4. Media
5. Contact & Support

Color pallets
#0053E0
#FF2500
#ffffff

Please see attachment for more detail

Target Market(s)

Churches and christian schools

Industry/Entity Type

magic, entertainment, christianity

Number of Pages Required

5+ page

Colors
0054AA
0677BA
7BADD7
CADEEF
E8F1F8

Requirements
Should not have
• - search bar

```html
<!DOCTYPE html>
<html lang="en">
<head>
<meta charset="utf-8">
<title>About Lanternfold – Lanternfold Ministries</title>
<link href="https://fonts.googleapis.com/css2?family=Montserrat:ital,wght@0,400;0,500;0,600;0,700;1,600;1,700&family=Patrick+Hand+SC&display=swap" rel="stylesheet">
<style>
:root{
  --ink:#222222;
  --text:#555555;
  --white:#ffffff;
  --blue:#0053e0;
  --red:#ff2500;
  --dark:#0b0b0e;
  --footer:#141414;
  --panel:#f3f4f8;
  --line:#3a3a3a;
}
*{box-sizing:border-box;margin:0;padding:0}
html,body{width:1200px;height:4042px;overflow:hidden}
body{font-family:'Montserrat',sans-serif;color:var(--text);background:var(--white);position:relative}
section,header,footer{position:absolute;left:0;width:1200px}
a{color:inherit;text-decoration:none}

/* Hero */
.hero{top:0;height:411px;background:var(--dark);overflow:hidden}
.hero-photo{position:absolute;left:360px;top:0;width:840px;height:411px;
  background:radial-gradient(ellipse at 30% 45%,#2c3a8a 0%,#16183a 35%,#0b0b12 70%),#0b0b12}
.hero-photo::after{content:"";position:absolute;left:0;bottom:0;width:100%;height:120px;
  background:linear-gradient(180deg,rgba(0,0,0,0) 0%,#3a2a22 100%)}
.brand{position:absolute;left:110px;top:24px;color:var(--white);font-weight:500;line-height:1}
.brand .name{display:block;font-size:40px;letter-spacing:.5px}
.brand .sub{display:block;font-size:28px;margin-top:6px}
.main-nav{position:absolute;left:450px;top:54px;display:flex;gap:24px;font-size:17px;font-weight:600;color:var(--white)}
.main-nav .current{color:var(--red)}
.hero-title{position:absolute;left:108px;top:160px;color:var(--white);font-size:52px;font-weight:700;line-height:1.2;letter-spacing:.5px}

/* Intro */
.intro{top:411px;height:408px;text-align:center}
.intro h1{margin:76px auto 0;width:960px;font-size:40px;font-weight:700;line-height:1.27;color:var(--ink)}
.intro p{margin:34px auto 0;width:780px;font-size:16.5px;line-height:1.62}

/* President */
.president{top:819px;height:998px;background:var(--panel)}
.role{font-family:'Patrick Hand SC',cursive;color:var(--blue)}
.president .role{position:absolute;left:108px;top:64px;font-size:32px}
.president h2{position:absolute;left:108px;top:108px;font-size:40px;font-weight:700;color:var(--ink)}
.president .bio{position:absolute;left:111px;top:170px;width:555px;font-size:16px;line-height:24px}
.bio p{margin-bottom:24px}
.portrait{position:absolute;left:715px;top:74px;width:377px;height:478px;
  background:radial-gradient(ellipse at 50% 40%,#8a6a58 0%,#3a2c28 35%,#0d0d0d 70%)}

/* Team */
.team{top:1817px;height:1564px}
.team h2{position:absolute;top:68px;width:100%;text-align:center;font-size:40px;font-weight:700;color:var(--ink)}
.member{position:absolute;left:111px;width:980px}
.member .photo{position:absolute;left:0;top:0;width:330px;height:386px}
.member .info{position:absolute;left:386px;top:6px;width:600px}
.member .role{font-size:22px;line-height:1}
.member h3{font-size:24px;font-weight:600;color:var(--ink);margin-top:6px}
.checks{list-style:none;margin-top:20px}
.checks li{position:relative;padding-left:24px;font-size:16.5px;line-height:18px;margin-bottom:14.5px}
.checks li svg{position:absolute;left:0;top:3px}
.m1{top:165px}.m2{top:620px}.m3{top:1072px}
.p1{background:linear-gradient(160deg,#9aa36b 0%,#7d5a48 30%,#3bb3c9 55%,#1c2333 80%)}
.p2{background:radial-gradient(ellipse at 50% 40%,#bcbcbc 0%,#5a5a5a 40%,#0e0e0e 75%)}
.p3{background:radial-gradient(ellipse at 50% 38%,#d9a07c 0%,#9a7a74 35%,#4d5f86 65%,#2b3857 100%)}

/* Quote */
.verse{top:3381px;height:272px;background:var(--red);color:var(--white);text-align:center}
.verse .mark{position:absolute;left:140px;top:44px}
.verse blockquote{position:absolute;left:150px;top:58px;width:900px;font-size:25px;font-style:italic;font-weight:600;line-height:35px}
.verse cite{position:absolute;left:0;top:200px;width:1200px;text-align:center;font-style:normal;font-weight:600;font-size:20px}

/* Footer */
.site-footer{top:3653px;height:389px;background:var(--footer);color:var(--white)}
.site-footer .brand{top:104px}
.site-footer .brand .name{font-size:60px}
.site-footer .brand .sub{font-size:44px;margin-top:10px}
.foot-col{position:absolute;top:68px;font-size:15.5px}
.foot-col h4{font-size:17px;font-weight:600;margin-bottom:18px}
.foot-col li{list-style:none;line-height:30px}
.links{left:500px}
.contact{left:757px}
.contact li{display:flex;align-items:center;gap:8px}
.divider{position:absolute;left:110px;top:282px;width:980px;height:1px;background:var(--line)}
.copyright{position:absolute;left:111px;top:322px;font-size:15.5px}
.social{position:absolute;left:1043px;top:307px;width:44px;height:44px;border:1.5px solid #777;border-radius:50%}
</style>
</head>
<body>

<header class="hero">
  <div class="hero-photo" role="img" aria-label="Performer with acoustic guitar on a stage in front of a lit sign with the ministry name, audience in the foreground"></div>
  <a class="brand" href="#"><span class="name">Lanternfold</span><span class="sub">Ministries</span></a>
  <nav class="main-nav">
    <a href="#">Home</a>
    <a href="#">Shows &amp; Skylark</a>
    <a href="#" class="current">About Lanternfold</a>
    <a href="#">Media</a>
    <a href="#">Contact &amp; Support</a>
  </nav>
  <h1 class="hero-title">ABOUT<br>LANTERNFOLD</h1>
</header>

<section class="intro">
  <h1>CHRISTIAN MINISTRY USING MAGIC, MUSIC AND MULTIMEDIA TO TEACH GOSPEL</h1>
  <p>Lorem ipsum dolor sit amet, consectetur adipiscing elit, sed do eiusmod tempor incididunt ut labore et dolore magna aliqua. Ut enim ad minim veniam, quis nostrud exercitation ullamco laboris nisi ut aliquip ex ea comodo consequat. Duis aute irure dolor in reprehenderit in vol uptate velit esse cillum dolore eu fugiat nulla pariatu pt eur sint occaecat cupidatat non proident, sunt in culpa qui officia deserunt mollit anim.</p>
</section>

<section class="president">
  <p class="role">President</p>
  <h2>OWEN HALLOWAY</h2>
  <div class="bio">
    <p>Owen Halloway began appearing professionally when he was just thirteen years of age. By sixteen, Halloway had embarked on a journey that would soon rocket him to the stages of hotels, theaters and luxury cruise ships worldwide. By twenty he had established himself as a truly international, master in the art of theatrical stage illusion. In his thirties, Halloway became a sought after entertainer and speaker for top corporations.</p>
    <p>Little did he know, his most important work was yet to reveal itself. In the midst of the bright lights of Las Vegas, Halloway felt a tug on his heart. As he struggled to understand, it soon became clear; God had other plans. God was calling Halloway to service, to a life of change and a commission with an eternal promise.</p>
    <p>Today Owen Halloway shares his God-given talents along with the energy and candor of his faith, in each "Lanternfold It!"... Celebration of Wonder. Through the focus of this unique ministry, God has blessed the lives of literally thousands of people who have made personal commitments to accept Jesus as their personal savior. Owen gives all glory to God. You'll be thrilled by his professional entertainment, inspired to hear the story of his exciting faith in Jesus Christ, and most importantly of all, to learn how this can become a reality for you!</p>
    <p>Owen is a member of The Guild of Stage Illusionists, The Fellowship of Gospel Illusionists and is a ridiculed member of Ironleaf Fitness.</p>
    <p style="margin-bottom:0">One more thing... Why does everyone call Owen Halloway, “Magic Boy?”</p>
    <p>It’s pretty funny, but you’ll have to ask Owen yourself!</p>
  </div>
  <div class="portrait" role="img" aria-label="Portrait of the ministry president smiling, wearing glasses and a black t-shirt"></div>
</section>

<section class="team">
  <h2>MEET OUR TEAM</h2>

  <article class="member m1">
    <div class="photo p1" role="img" aria-label="Portrait of the secretary treasurer seated outdoors on a patio"></div>
    <div class="info">
      <p class="role">Secretary Treasurer</p>
      <h3>Marla Penwick</h3>
      <ul class="checks">
        <li><svg width="14" height="12" viewBox="0 0 14 12"><path d="M1 6.5l4 4L13 1.5" fill="none" stroke="#ff2500" stroke-width="2.6"/></svg>Co-Founder of Lanternfold Ministries Inc. (2007-present)</li>
        <li><svg width="14" height="12" viewBox="0 0 14 12"><path d="M1 6.5l4 4L13 1.5" fill="none" stroke="#ff2500" stroke-width="2.6"/></svg>Mission Coordinator and Trainer for Mexico, Cedar Hollow United Methodist Church, 2003</li>
        <li><svg width="14" height="12" viewBox="0 0 14 12"><path d="M1 6.5l4 4L13 1.5" fill="none" stroke="#ff2500" stroke-width="2.6"/></svg>Speaker to women’s groups in churches</li>
        <li><svg width="14" height="12" viewBox="0 0 14 12"><path d="M1 6.5l4 4L13 1.5" fill="none" stroke="#ff2500" stroke-width="2.6"/></svg>Member of Praise Team, Cedar Hollow United Methodist Church</li>
        <li><svg width="14" height="12" viewBox="0 0 14 12"><path d="M1 6.5l4 4L13 1.5" fill="none" stroke="#ff2500" stroke-width="2.6"/></svg>Bachelor Science in Home Economics - (Brightwater University)</li>
        <li><svg width="14" height="12" viewBox="0 0 14 12"><path d="M1 6.5l4 4L13 1.5" fill="none" stroke="#ff2500" stroke-width="2.6"/></svg>Account executive in Sales and Marketing (Verona Lane Cosmetics)</li>
        <li><svg width="14" height="12" viewBox="0 0 14 12"><path d="M1 6.5l4 4L13 1.5" fill="none" stroke="#ff2500" stroke-width="2.6"/></svg>Account executive in Sales and Marketing (Tickwell Watch)</li>
        <li><svg width="14" height="12" viewBox="0 0 14 12"><path d="M1 6.5l4 4L13 1.5" fill="none" stroke="#ff2500" stroke-width="2.6"/></svg>Founder of Steady Step Seminars</li>
        <li><svg width="14" height="12" viewBox="0 0 14 12"><path d="M1 6.5l4 4L13 1.5" fill="none" stroke="#ff2500" stroke-width="2.6"/></svg>Professional speaker and trainer (1990-present)</li>
        <li><svg width="14" height="12" viewBox="0 0 14 12"><path d="M1 6.5l4 4L13 1.5" fill="none" stroke="#ff2500" stroke-width="2.6"/></svg>Hobbies - Gardening/Landscaping, Cooking, Sewing</li>
      </ul>
    </div>
  </article>

  <article class="member m2">
    <div class="photo p2" role="img" aria-label="Black and white portrait of a director in a plaid shirt"></div>
    <div class="info">
      <p class="role">Director</p>
      <h3>Dale Ostrander</h3>
      <ul class="checks">
        <li><svg width="14" height="12" viewBox="0 0 14 12"><path d="M1 6.5l4 4L13 1.5" fill="none" stroke="#ff2500" stroke-width="2.6"/></svg>Northgate Architects, Atlanta - 36 years</li>
        <li><svg width="14" height="12" viewBox="0 0 14 12"><path d="M1 6.5l4 4L13 1.5" fill="none" stroke="#ff2500" stroke-width="2.6"/></svg>Bachelor of Architecture - Pinecrest University</li>
        <li><svg width="14" height="12" viewBox="0 0 14 12"><path d="M1 6.5l4 4L13 1.5" fill="none" stroke="#ff2500" stroke-width="2.6"/></svg>Master of Architecture - Lakeshore State University</li>
        <li><svg width="14" height="12" viewBox="0 0 14 12"><path d="M1 6.5l4 4L13 1.5" fill="none" stroke="#ff2500" stroke-width="2.6"/></svg>Former Elder and Deacon - Meadowbrook Presbyterian Church</li>
        <li><svg width="14" height="12" viewBox="0 0 14 12"><path d="M1 6.5l4 4L13 1.5" fill="none" stroke="#ff2500" stroke-width="2.6"/></svg>Greeter team - Cedar Hollow United Methodist Church</li>
        <li><svg width="14" height="12" viewBox="0 0 14 12"><path d="M1 6.5l4 4L13 1.5" fill="none" stroke="#ff2500" stroke-width="2.6"/></svg>Hobbies - Grandchildren</li>
      </ul>
    </div>
  </article>

  <article class="member m3">
    <div class="photo p3" role="img" aria-label="Studio portrait of a director in a suit and tie"></div>
    <div class="info">
      <p class="role">Director</p>
      <h3>Barrett Lund</h3>
      <ul class="checks">
        <li><svg width="14" height="12" viewBox="0 0 14 12"><path d="M1 6.5l4 4L13 1.5" fill="none" stroke="#ff2500" stroke-width="2.6"/></svg>Co-Founder of Lanternfold Ministries Inc. (2007-present)</li>
        <li><svg width="14" height="12" viewBox="0 0 14 12"><path d="M1 6.5l4 4L13 1.5" fill="none" stroke="#ff2500" stroke-width="2.6"/></svg>Mission Coordinator and Trainer for Mexico, Cedar Hollow United Methodist Church, 2003</li>
        <li><svg width="14" height="12" viewBox="0 0 14 12"><path d="M1 6.5l4 4L13 1.5" fill="none" stroke="#ff2500" stroke-width="2.6"/></svg>Speaker to women’s groups in churches</li>
        <li><svg width="14" height="12" viewBox="0 0 14 12"><path d="M1 6.5l4 4L13 1.5" fill="none" stroke="#ff2500" stroke-width="2.6"/></svg>Member of Praise Team, Cedar Hollow United Methodist Church</li>
        <li><svg width="14" height="12" viewBox="0 0 14 12"><path d="M1 6.5l4 4L13 1.5" fill="none" stroke="#ff2500" stroke-width="2.6"/></svg>Bachelor Science in Home Economics - (Brightwater University)</li>
        <li><svg width="14" height="12" viewBox="0 0 14 12"><path d="M1 6.5l4 4L13 1.5" fill="none" stroke="#ff2500" stroke-width="2.6"/></svg>Account executive in Sales and Marketing (Verona Lane Cosmetics)</li>
        <li><svg width="14" height="12" viewBox="0 0 14 12"><path d="M1 6.5l4 4L13 1.5" fill="none" stroke="#ff2500" stroke-width="2.6"/></svg>Account executive in Sales and Marketing (Tickwell Watch)</li>
        <li><svg width="14" height="12" viewBox="0 0 14 12"><path d="M1 6.5l4 4L13 1.5" fill="none" stroke="#ff2500" stroke-width="2.6"/></svg>Founder of Steady Step Seminars</li>
        <li><svg width="14" height="12" viewBox="0 0 14 12"><path d="M1 6.5l4 4L13 1.5" fill="none" stroke="#ff2500" stroke-width="2.6"/></svg>Professional speaker and trainer (1990-present)</li>
        <li><svg width="14" height="12" viewBox="0 0 14 12"><path d="M1 6.5l4 4L13 1.5" fill="none" stroke="#ff2500" stroke-width="2.6"/></svg>Hobbies - Gardening/Landscaping, Cooking, Sewing</li>
      </ul>
    </div>
  </article>
</section>

<section class="verse">
  <svg class="mark" width="84" height="64" viewBox="0 0 84 64" aria-hidden="true">
    <path d="M4 62 L20 8 Q24 0 34 2 L40 4 L26 62 Z M44 62 L60 8 Q64 0 74 2 L80 4 L66 62 Z" fill="#ffffff" fill-opacity=".35"/>
  </svg>
  <blockquote>“But you shall receive power when the Holy Spirit has come upon you; and you shall be witnesses to Me in Jerusalem, and in all Judea and Samaria, and to the end of the earth.”</blockquote>
  <cite>Acts 1:8</cite>
</section>

<footer class="site-footer">
  <a class="brand" href="#"><span class="name">Lanternfold</span><span class="sub">Ministries</span></a>
  <div class="foot-col links">
    <h4>Quick Links</h4>
    <ul>
      <li><a href="#">Home</a></li>
      <li><a href="#">Shows &amp; Skylark</a></li>
      <li><a href="#">About Lanternfold</a></li>
      <li><a href="#">Media</a></li>
      <li><a href="#">Contact &amp; Support</a></li>
    </ul>
  </div>
  <div class="foot-col contact">
    <h4>Contact Us</h4>
    <ul>
      <li>Lanternfold Ministries Inc.</li>
      <li><svg width="10" height="14" viewBox="0 0 10 14"><path d="M5 0a5 5 0 0 0-5 5c0 3.6 5 9 5 9s5-5.4 5-9a5 5 0 0 0-5-5zm0 7a2 2 0 1 1 0-4 2 2 0 0 1 0 4z" fill="#ff2500"/></svg>Harrow Falls, Georgia, USA</li>
      <li><svg width="13" height="13" viewBox="0 0 24 24"><path d="M6.6 10.8a15.1 15.1 0 0 0 6.6 6.6l2.2-2.2a1 1 0 0 1 1-.25 11.4 11.4 0 0 0 3.6.57 1 1 0 0 1 1 1V20a1 1 0 0 1-1 1A17 17 0 0 1 3 4a1 1 0 0 1 1-1h3.5a1 1 0 0 1 1 1c0 1.250.2 2.45.57 3.57a1 1 0 0 1-.25 1z" fill="#ff2500"/></svg>555-014-2286</li>
      <li><svg width="15" height="11" viewBox="0 0 15 11"><rect width="15" height="11" rx="1" fill="#ff2500"/><path d="M0.5 1l7 5 7-5" fill="none" stroke="#141414" stroke-width="1.3"/></svg>Email Us</li>
    </ul>
  </div>
  <div class="divider"></div>
  <p class="copyright">Copyright © - 2023 Lanternfold Ministries Inc., All Rights Reserved</p>
  <span class="social" aria-hidden="true"></span>
</footer>

</body>
</html>
```